Business Card design for Property Developer

We need a business card design for a Melbourne based Property Developer called "Kestrelmoor Holdings Pty Ltd".

We subdivide land and onsell to builders etc.

We already have a company logo, which is attached. Also I have attached the layout requirements from the printer. We would like a 2-sided design with one side displaying our logo by itself and the other with the required info, such as name, address, tel no., email, abn etc. The card will need to be used by 4 members of staff so name and contact details should be interchangable.
Updates

If possible, can you please write "name' "job position" "phone" "email" "address" on the card but leave them so I can add the details at a later time. Thank you. Also I plan on printing with UV spot printing as a background on the card. Keep this is mind when designing.

Thanks again.

Hello designers, please do not include pics of houses, house plansĀ or construction machinery etc as we really do not like the way it looks. Thank you.

Target Market(s)

Real Estate Agents, Land Owners, Local Council Departments, Govt Bodies, other Developers etc.

Industry/Entity Type

Business

Requirements
Must have
• 2-sided design with one side displaying our logo by itself and the other with the required info, such as name, address, tel no., email, abn etc.

```html
<!DOCTYPE html>
<html lang="en">
<head>
<meta charset="utf-8">
<title>Kestrelmoor Holdings – Business Card</title>
<link rel="stylesheet" href="https://fonts.googleapis.com/css2?family=Arimo:wght@700&display=swap">
<style>
  :root {
    --page-bg: #ffffff;
    --frame: #e8e8e8;
    --card-bg: #ffffff;
    --brand-blue: #1d4f9c;
    --brand-red: #c8141c;
    --wave-light: #19b6ef;
    --wave-mid: #0b72c9;
    --wave-dark: #0a3f9a;
    --text-light: #ffffff;
  }
  * { margin: 0; padding: 0; box-sizing: border-box; }
  html, body {
    width: 920px;
    height: 1200px;
    overflow: hidden;
    background: var(--page-bg);
    font-family: "Arimo", Arial, sans-serif;
    font-weight: 700;
  }
  .card {
    position: absolute;
    left: 28px;
    width: 864px;
    height: 542px;
    border: 16px solid var(--frame);
    background: var(--card-bg);
    overflow: hidden;
  }
  .card--info { top: 28px; }
  .card--logo { top: 626px; }

  .wave {
    position: absolute;
    inset: 0;
    width: 832px;
    height: 510px;
  }

  .brand {
    position: absolute;
    display: flex;
    flex-direction: column;
    align-items: center;
    color: var(--brand-red);
    text-transform: uppercase;
    text-align: center;
    line-height: 1.05;
  }
  .brand__mark {
    border-radius: 50%;
    background: var(--brand-blue);
  }
  .brand--small {
    left: 26px;
    top: 176px;
    width: 280px;
    font-size: 28px;
  }
  .brand--small .brand__mark { width: 96px; height: 96px; margin-bottom: 22px; }
  .brand--large {
    left: 0;
    right: 0;
    top: 128px;
    font-size: 46px;
  }
  .brand--large .brand__mark { width: 176px; height: 176px; margin-bottom: 30px; }

  .details {
    position: absolute;
    right: 38px;
    text-align: right;
    color: var(--text-light);
  }
  .details__name { top: 44px; font-size: 29px; line-height: 1.15; }
  .details__role { font-size: 22px; }
  .details__address { top: 182px; font-size: 20px; line-height: 1.4; }
  .details__contact { top: 364px; font-size: 24px; line-height: 1.33; }
</style>
</head>
<body>
  <section class="card card--info" aria-label="Business card front">
    <svg class="wave" viewBox="0 0 832 510" aria-hidden="true">
      <defs>
        <linearGradient id="waveFill" x1="0" y1="0" x2="0.3" y2="1">
          <stop offset="0" stop-color="var(--wave-light)"/>
          <stop offset="0.5" stop-color="var(--wave-mid)"/>
          <stop offset="1" stop-color="var(--wave-dark)"/>
        </linearGradient>
      </defs>
      <path d="M497 0 C455 45 470 110 430 185 C392 255 352 300 350 400 L346 510 L832 510 L832 0 Z" fill="url(#waveFill)"/>
    </svg>

    <div class="brand brand--small">
      <span class="brand__mark" aria-hidden="true"></span>
      <span class="brand__name">Kestrelmoor<br>Holdings</span>
    </div>

    <div class="details details__name">Your Name<div class="details__role">Job Position</div></div>
    <address class="details details__address" style="font-style:normal">123 Street Name,<br>County, City,<br>State 88888 USA</address>
    <div class="details details__contact">
      M: 123 456 7890<br>
      P: 123 456 7890<br>
      E: name@domain.com<br>
      W: www.domain.com
    </div>
  </section>

  <section class="card card--logo" aria-label="Business card back">
    <div class="brand brand--large">
      <span class="brand__mark" aria-hidden="true"></span>
      <span class="brand__name">Kestrelmoor Holdings</span>
    </div>
  </section>
</body>
</html>
```